Harwick Recovery Centre Tailormade Training

We are wanting to promote our Training Unit and in particular tailor made training. We want our name - Harwick Recovery Centre - to be prominent and to include the bullet points from attached file plus other content as seems useful from the file. We need the PCS logo and Trust name at the bottom using PCS blue - other modern colours to blend in with this. Some graphics and modern design. Overall message: quality training at reasonable cost tailored to agency needs.

Target Market(s)

Agencies providing services for people with alcohol and drug problems

Industry/Entity Type

Health Care

Font styles to use
Sans Serif

Colors
f37122
85cae6
fbf289

Requirements
Must have
• Harwick Recovery Centre
• We will......
•  Support your organisation to develop a training plan and work with you to design the course content.
•  Assign a member of our team to liaise with you through- out the programme.
•  Provide experienced and qualified teaching staff to de- liver your training.
• For further information and prices please contact
• Colin Marsby, Training Department Manager
• Harwick Recovery Centre, 42 Brackenhill Row, Leeds LS7 3QD telephone 0113 4720368 hrc@vantorel.ac.uk
• PCS logo with Trust name - see bottom of attached file - use exact PCS blue
Nice to have
• Modern colours to tone with PCS blue
• Some graphics or bold background
• Emphasis is on the training but needs a connection to addictions
Should not have
• Nothing stereotyped of problem drinkers or drug users

```html
<!DOCTYPE html>
<html lang="en">
<head>
<meta charset="utf-8">
<title>Harwick Recovery Centre Training</title>
<link rel="stylesheet" href="https://fonts.googleapis.com/css2?family=Roboto+Condensed:wght@400;700&family=Lato:wght@400;700&display=swap">
<style>
  :root {
    --blue: #1a8fe0;
    --blue-deep: #0f6fc4;
    --pcs-blue: #005eb8;
    --orange: #f37122;
    --orange-dark: #b84f12;
    --dark: #2a2a2a;
    --dark-2: #3a3a3a;
    --ink: #333333;
    --ink-dark: #1e1e1e;
    --white: #ffffff;
    --paper: #f3f6f9;
  }
  * { box-sizing: border-box; margin: 0; padding: 0; }
  html, body { width: 872px; height: 1200px; overflow: hidden; background: var(--white); }
  .flyer {
    position: relative; width: 872px; height: 1200px; overflow: hidden;
    background: linear-gradient(160deg, var(--white) 40%, var(--paper) 100%);
    font-family: "Lato", sans-serif; color: var(--ink);
  }
  .hero-art { position: absolute; left: 0; top: 0; }

  .title-line { position: absolute; left: 26px; font-family: "Roboto Condensed", sans-serif; line-height: 1; white-space: nowrap; }
  .title-main { top: 24px; font-size: 86px; font-weight: 700; color: var(--white); letter-spacing: -1px; }
  .title-sub { top: 128px; font-size: 50px; font-weight: 400; color: var(--ink-dark); }
  .title-tail { top: 190px; font-size: 36px; font-weight: 400; color: var(--white); }

  .intro { position: absolute; left: 23px; top: 449px; width: 318px; font-size: 16.5px; line-height: 20.5px; color: var(--ink); }
  .feature { position: absolute; left: 0; width: 360px; }
  .feature-tag {
    display: inline-block; height: 34px; padding: 0 38px 0 23px; line-height: 34px;
    background: var(--blue); color: var(--white);
    font-family: "Roboto Condensed", sans-serif; font-weight: 700; font-size: 21px; letter-spacing: .3px;
    clip-path: polygon(0 0, 100% 0, calc(100% - 18px) 100%, 0 100%);
  }
  .feature-text { margin: 14px 0 0 23px; width: 310px; font-size: 16.5px; line-height: 20.5px; }

  .panel {
    position: absolute; left: 421px; top: 401px; width: 451px; height: 682px;
    background: linear-gradient(180deg, var(--dark-2), var(--dark) 60%, #262626);
  }
  .band {
    position: absolute; background: var(--orange);
    font-family: "Roboto Condensed", sans-serif; font-weight: 700; color: var(--white);
    letter-spacing: 1px; white-space: nowrap;
  }
  .band-will { left: 392px; top: 401px; width: 480px; height: 80px; font-size: 56px; line-height: 82px; padding-left: 72px; }
  .band-services { left: 406px; top: 707px; width: 307px; height: 54px; font-size: 54px; line-height: 56px; padding-left: 57px;
    clip-path: polygon(0 0, 100% 0, calc(100% - 22px) 100%, 0 100%); }
  .fold { position: absolute; }

  .list { position: absolute; list-style: none; color: var(--white); font-weight: 700; white-space: nowrap; }
  .list li { position: relative; padding-left: 20px; }
  .list li::before { content: ""; position: absolute; left: 0; width: 10px; height: 10px; border-radius: 50%; background: var(--orange); }
  .pledges { left: 470px; top: 500px; font-size: 18.5px; line-height: 23.6px; }
  .pledges li { margin-bottom: 5px; }
  .pledges li::before { top: 7px; }
  .services { left: 470px; top: 778px; font-size: 18.5px; line-height: 23.6px; }
  .services li::before { top: 7px; }

  .trust { position: absolute; left: 23px; top: 1064px; display: flex; align-items: center; gap: 14px; }
  .trust-name { font-size: 44px; font-weight: 700; color: var(--pcs-blue); letter-spacing: 1px; line-height: 48px; }
  .trust-partner { font-size: 18px; font-weight: 700; color: var(--ink-dark); }
  .manager { position: absolute; right: 30px; top: 1101px; font-size: 16.5px; font-weight: 700; color: var(--blue); white-space: nowrap; }

  .contact-bar {
    position: absolute; left: 0; bottom: 0; width: 872px; height: 56px; background: var(--orange);
    display: flex; align-items: center; justify-content: center; gap: 13px;
    color: var(--white); font-size: 17px; font-weight: 700; white-space: nowrap;
  }
  .contact-item { display: flex; align-items: center; gap: 6px; }
  .contact-item svg { flex: none; }
</style>
</head>
<body>
<div class="flyer">
  <svg class="hero-art" width="872" height="440" viewBox="0 0 872 440">
    <defs>
      <linearGradient id="meeting" x1="0" y1="0" x2="1" y2="1">
        <stop offset="0" stop-color="#e9eef2"/>
        <stop offset=".55" stop-color="#b9c4cf"/>
        <stop offset="1" stop-color="#6e7885"/>
      </linearGradient>
      <linearGradient id="tablet" x1="0" y1="0" x2="1" y2="1">
        <stop offset="0" stop-color="#d8dee3"/>
        <stop offset="1" stop-color="#9ba7b2"/>
      </linearGradient>
      <linearGradient id="blueFill" x1="0" y1="0" x2="1" y2="1">
        <stop offset="0" stop-color="#2a9cf0"/>
        <stop offset="1" stop-color="#0f7fd6"/>
      </linearGradient>
    </defs>
    <rect x="0" y="0" width="872" height="401" fill="url(#meeting)" role="img" aria-label="Photo of professionals meeting around a table with a laptop and shaking hands"/>
    <polygon points="0,0 360,0 420,416 0,416" fill="url(#blueFill)"/>
    <polygon points="0,255 352,255 380,404 0,404" fill="url(#tablet)" role="img" aria-label="Photo of a hand using a tablet showing charts"/>
    <polygon points="0,421 412,421 414,430 0,430" fill="var(--orange)"/>
  </svg>

  <span class="title-line title-main">HARWICK</span>
  <span class="title-line title-sub">RECOVERY</span>
  <span class="title-line title-tail">CENTRE TRAINING</span>

  <p class="intro">Your organisation may require training for health and social care professionals concerned with the management of substance misuse issues. We can address your specific needs, with the location, timing and course content designed to suit your training objectives.</p>

  <div class="feature" style="top:616px">
    <span class="feature-tag">TAILORED CONTENT</span>
    <p class="feature-text">Work with us to develop a course that meets your specific requirements.</p>
  </div>
  <div class="feature" style="top:726px">
    <span class="feature-tag">CONFIDENTIAL</span>
    <p class="feature-text">Staff can explore issues relevant to your area of work.</p>
  </div>
  <div class="feature" style="top:834px">
    <span class="feature-tag">FLEXIBLE</span>
    <p class="feature-text">Staff can explore issues relevant to your area of work.</p>
  </div>
  <div class="feature" style="top:941px">
    <span class="feature-tag">LOCATION</span>
    <p class="feature-text">Bring the course in-house or use our fully serviced training facility.</p>
  </div>

  <div class="panel"></div>

  <div class="band band-will">WE WILL...</div>
  <svg class="fold" style="left:392px;top:481px" width="29" height="22" viewBox="0 0 29 22"><polygon points="0,0 29,0 29,22" fill="var(--orange-dark)"/></svg>

  <ul class="list pledges">
    <li>Support your organisation to develop<br>a training plan and work with you to<br>design the course content</li>
    <li>Assign a member of our team to liaise<br>with you throughout the programme</li>
    <li>Provide experienced and qualified<br>teaching staff to deliver your training</li>
  </ul>

  <div class="band band-services">SERVICES</div>
  <svg class="fold" style="left:406px;top:761px" width="15" height="14" viewBox="0 0 15 14"><polygon points="0,0 15,0 15,14" fill="var(--orange-dark)"/></svg>

  <ul class="list services">
    <li>Dual Diagnosis</li>
    <li>Continuing Professional<br>Development</li>
    <li>Harm Reduction</li>
    <li>Social Behaviour<br>and Network Therapy</li>
    <li>Psychopharmacology</li>
    <li>Motivational Interviewing</li>
    <li>Assessment</li>
    <li>Cognitive Behavioural</li>
    <li>Coping Skills</li>
    <li>Interventions</li>
  </ul>

  <div class="trust">
    <span class="trust-name">PCS</span>
    <span class="trust-partner">Brackenhill Care Partnership</span>
  </div>
  <p class="manager">Colin Marsby, Training Department Manager</p>

  <div class="contact-bar">
    <span class="contact-item">
      <svg width="16" height="16" viewBox="0 0 24 24"><path fill="#fff" d="M6.6 10.8a15.1 15.1 0 0 0 6.6 6.6l2.2-2.2a1 1 0 0 1 1-.25 11.4 11.4 0 0 0 3.6.57 1 1 0 0 1 1 1V20a1 1 0 0 1-1 1A17 17 0 0 1 3 4a1 1 0 0 1 1-1h3.5a1 1 0 0 1 1 1c0 1.25.2 2.450.57 3.6a1 1 0 0 1-.25 1z"/></svg>
      0113 4720368
    </span>
    <span class="contact-item">
      <svg width="16" height="12" viewBox="0 0 16 12"><rect width="16" height="12" rx="1" fill="#fff"/><path d="M1 1l7 6 7-6" stroke="var(--orange)" stroke-width="1.5" fill="none"/></svg>
      hrc@vantorel.ac.uk
    </span>
    <span class="contact-item">
      <svg width="13" height="18" viewBox="0 0 13 18"><path fill="#fff" d="M6.5 0A6.5 6.5 0 0 0 0 6.5C0 11.4 6.5 18 6.5 18S13 11.4 13 6.5A6.5 6.5 0 0 0 6.5 0zm0 9A2.5 2.5 0 1 1 6.5 4a2.5 2.5 0 0 1 0 5z"/></svg>
      Harwick Recovery Centre, 42 Brackenhill Row, Leeds LS7 3QD
    </span>
  </div>
</div>
</body>
</html>
```